Business Card Design

I'm a commercial general contractor remodel offices, hotels, health clubs and stores mostly San Francisco and the peninsula
the file I down loaded is kind of what I want I like the I beam with my company name in it, that would be fine with me but if you have better Idea will look at it you never know, I'm decided to give in and change my company name to how every one knows me, I have been in business since 1991, I like the I beam logo I included one of my old card from my old company for reference for you.

Industry/Entity Type

Business

Contact Information for Business Card

BRAXO CONSTRUCTION (is my company name)
Wendell Trusk contractor, LIc 314827
4158 Garnet Row, San Bruno, California 94066
mobile, (415) 555-0147
phone (650) 555-0182
Fax, (650) 555-0183
email, braxo@braxoconstruction.example

```html
<!DOCTYPE html>
<html lang="en">
<head>
<meta charset="utf-8">
<title>Braxo Construction – Business Card</title>
<link rel="stylesheet" href="https://fonts.googleapis.com/css2?family=Montserrat:wght@400;500&display=swap">
<style>
  :root {
    --backdrop: #b9b9b7;
    --card: #0d0d0d;
    --card-edge: #1c1c1c;
    --accent: #1f8ad6;
    --ink: #f2f2f2;
    --rule: #2a2a2a;
  }
  * { margin: 0; padding: 0; box-sizing: border-box; }
  html, body { width: 1200px; height: 900px; overflow: hidden; }
  body {
    background: var(--backdrop);
    font-family: "Montserrat", sans-serif;
    display: flex;
    flex-direction: column;
    align-items: center;
    justify-content: center;
    gap: 44px;
  }
  .card {
    width: 700px;
    height: 400px;
    background: radial-gradient(ellipse at 50% 40%, var(--card-edge), var(--card) 70%);
    position: relative;
    box-shadow: 0 10px 24px rgba(0,0,0,.25);
  }
  .card--front {
    display: flex;
    align-items: center;
    justify-content: center;
  }
  .brand {
    display: flex;
    align-items: center;
    gap: 14px;
    color: var(--ink);
    font-weight: 500;
    letter-spacing: 2px;
  }
  .brand__mark {
    width: 22px; height: 22px;
    background: var(--accent);
  }
  .brand--front .brand__name { font-size: 30px; }
  .brand--back { position: absolute; top: 70px; right: 56px; }
  .brand--back .brand__name { font-size: 20px; }
  .holder { position: absolute; left: 44px; top: 112px; }
  .holder__name {
    color: var(--accent);
    font-size: 26px;
    font-weight: 500;
    margin-bottom: 6px;
  }
  .holder__role { color: var(--ink); font-size: 16px; line-height: 1.3; }
  .divider {
    position: absolute;
    left: 44px; right: 56px; top: 200px;
    height: 1px;
    background: var(--rule);
  }
  .contacts {
    position: absolute;
    right: 40px; bottom: 34px;
    list-style: none;
    text-align: right;
  }
  .contacts li {
    display: flex;
    justify-content: flex-end;
    align-items: center;
    gap: 14px;
    color: var(--ink);
    font-size: 18px;
    line-height: 29px;
  }
  .contacts svg { width: 14px; height: 14px; fill: var(--accent); flex: none; }
</style>
</head>
<body>

<section class="card card--front">
  <div class="brand brand--front">
    <span class="brand__mark"></span>
    <span class="brand__name">BRAXO CONSTRUCTION</span>
  </div>
</section>

<section class="card card--back">
  <div class="brand brand--back">
    <span class="brand__mark"></span>
    <span class="brand__name">BRAXO CONSTRUCTION</span>
  </div>

  <div class="holder">
    <p class="holder__name">Wendell Trusk</p>
    <p class="holder__role">Contractor,<br>LIc 314827</p>
  </div>

  <div class="divider"></div>

  <ul class="contacts">
    <li>(415) 555-0147
      <svg viewBox="0 0 14 14" aria-label="mobile"><path d="M4 0h6a1 1 0 0 1 1 1v12a1 1 0 0 1-1 1H4a1 1 0 0 1-1-1V1a1 1 0 0 1 1-1zm0 2v9h6V2z"/></svg></li>
    <li>(650) 555-0182
      <svg viewBox="0 0 14 14" aria-label="phone"><path d="M1 4c0-2 2-3 6-3s6 1 6 3v1H9V3.5H5V5H1zm2 2h8l2 6H1z"/></svg></li>
    <li>(650) 555-0183
      <svg viewBox="0 0 14 14" aria-label="fax"><path d="M4 1h6v3H4zM1 5h12v8H1zm3 3v2h6V8z"/></svg></li>
    <li>braxo@braxoconstruction.example
      <svg viewBox="0 0 14 14" aria-label="email"><path d="M0 3h14v9H0zm1 1v.5l6 4 6-4V4z"/></svg></li>
    <li>4158 Garnet Row, San Bruno, California 94066
      <svg viewBox="0 0 14 14" aria-label="address"><path d="M7 0a5 5 0 0 1 5 5c0 4-5 9-5 9S2 9 2 5a5 5 0 0 1 5-5zm0 3a2 2 0 1 0 0 4 2 2 0 0 0 0-4z"/></svg></li>
  </ul>
</section>

</body>
</html>
```